Bref créative
TMB Business Cards and Stationary
Professional
Marcus Elsby
General Manager
2716 Bellhaven Lane
Simi Valley, CA 93063
marcus@tobinmillbuilders.example

```html
<!DOCTYPE html>
<html lang="en">
<head>
<meta charset="utf-8">
<title>TMB Stationery Concepts</title>
<link href="https://fonts.googleapis.com/css2?family=Montserrat:wght@400;700&display=swap" rel="stylesheet">
<style>
:root{
  --bg:#ece7df;
  --paper:#ffffff;
  --green:#2f9a2a;
  --green-light:#7fcf3c;
  --green-dark:#17631a;
  --ink:#1a1a1a;
  --muted:#8a8a8a;
  --faint:#e4e8e4;
  --label:#6b6258;
}
*{margin:0;padding:0;box-sizing:border-box}
html,body{width:1200px;height:446px;overflow:hidden;background:var(--bg);font-family:"Montserrat",sans-serif;color:var(--ink)}
.canvas{position:relative;width:1200px;height:446px}
.sheet{position:absolute;background:var(--paper);box-shadow:0 2px 6px rgba(0,0,0,.18);overflow:hidden}
.sheet svg.wave{position:absolute;left:0;width:100%}
.label{position:absolute;font-size:6px;letter-spacing:.12em;text-transform:uppercase;color:var(--label);text-align:center}
.brand{display:flex;align-items:center;gap:3px;font-weight:700;color:var(--green-dark);line-height:1}
.brand .dot{border-radius:50%;background:var(--green)}
.brand-stack{display:flex;flex-direction:column;align-items:center;font-weight:700;color:var(--green-dark);line-height:1}
.brand-stack .dot{border-radius:50%;background:var(--green);margin-bottom:2px}
.brand-stack .corp{color:var(--ink);letter-spacing:.2em}
.watermark{position:absolute;font-weight:700;color:var(--faint);text-align:center;width:100%;line-height:1}
.contact{position:absolute;font-size:3.4px;line-height:1.5;color:var(--muted)}
</style>
</head>
<body>
<main class="canvas">
  <p class="label" style="left:8px;top:126px;width:100px;text-align:left">Stationery Concepts</p>

  <!-- business card front -->
  <section class="sheet business-card" style="left:12px;top:152px;width:96px;height:58px">
    <div class="brand" style="position:absolute;left:8px;top:18px;font-size:9px"><span class="dot" style="width:7px;height:7px"></span>TMB</div>
    <div class="contact" style="left:44px;top:14px">Marcus Elsby<br>General Manager<br>2716 Bellhaven Lane<br>Simi Valley, CA 93063<br>marcus@tobinmillbuilders.example</div>
    <svg class="wave" style="bottom:0;height:14px" viewBox="0 0 100 14" preserveAspectRatio="none"><defs><linearGradient id="gc" x1="0" x2="1"><stop offset="0" stop-color="var(--green-dark)"/><stop offset=".6" stop-color="var(--green)"/><stop offset="1" stop-color="var(--green-light)"/></linearGradient></defs><path d="M0 14V8Q50 0 100 6V14Z" fill="url(#gc)"/><path d="M0 7Q50 -1 100 5" stroke="var(--ink)" stroke-width="1" fill="none"/></svg>
  </section>
  <p class="label" style="left:12px;top:215px;width:96px">Business Card Front</p>

  <!-- business card back -->
  <section class="sheet business-card" style="left:12px;top:240px;width:96px;height:58px">
    <div class="brand-stack" style="position:absolute;left:0;width:100%;top:15px;font-size:9px"><span class="dot" style="width:8px;height:8px"></span>TMB<span class="corp" style="font-size:4px;margin-top:1px">Corp</span></div>
    <svg class="wave" style="bottom:0;height:10px" viewBox="0 0 100 10" preserveAspectRatio="none"><path d="M0 10V6Q50 0 100 4V10Z" fill="url(#gc)"/></svg>
  </section>
  <p class="label" style="left:12px;top:303px;width:96px">Business Card Back</p>

  <!-- letterhead 1 -->
  <section class="sheet letterhead" style="left:163px;top:19px;width:293px;height:394px">
    <div class="brand-stack" style="position:absolute;left:0;width:100%;top:22px;font-size:13px"><span class="dot" style="width:12px;height:12px"></span>TMB<span class="corp" style="font-size:5px;margin-top:2px">Corp</span></div>
    <div class="contact" style="right:14px;top:22px;text-align:left">2716 Bellhaven Lane<br>Simi Valley, CA 93063<br>marcus@tobinmillbuilders.example<br>Marcus Elsby</div>
    <div class="watermark" style="top:150px;font-size:64px">TMB</div>
    <svg class="wave" style="bottom:0;height:70px" viewBox="0 0 300 70" preserveAspectRatio="none"><path d="M0 70V30Q140 60 300 8V70Z" fill="url(#gc)"/><path d="M0 24Q140 56 300 2" stroke="var(--ink)" stroke-width="3" fill="none"/></svg>
  </section>
  <p class="label" style="left:163px;top:420px;width:293px">Letterhead Option 1</p>

  <!-- letterhead 2 -->
  <section class="sheet letterhead" style="left:475px;top:19px;width:298px;height:394px">
    <svg class="wave" style="top:0;height:34px" viewBox="0 0 300 34" preserveAspectRatio="none"><path d="M0 0H150Q60 6 0 34Z" fill="url(#gc)"/><path d="M0 30Q60 4 160 0" stroke="var(--ink)" stroke-width="2" fill="none"/></svg>
    <div class="brand-stack" style="position:absolute;left:0;width:100%;top:22px;font-size:13px"><span class="dot" style="width:12px;height:12px"></span>TMB<span class="corp" style="font-size:5px;margin-top:2px">Corp</span></div>
    <div class="watermark" style="top:150px;font-size:64px">TMB</div>
    <svg class="wave" style="bottom:0;height:70px" viewBox="0 0 300 70" preserveAspectRatio="none"><path d="M0 70V30Q140 60 300 8V70Z" fill="url(#gc)"/><path d="M0 24Q140 56 300 2" stroke="var(--ink)" stroke-width="3" fill="none"/></svg>
  </section>
  <p class="label" style="left:475px;top:420px;width:298px">Letterhead Option 2</p>

  <!-- envelope back dark flap -->
  <section class="sheet envelope" style="left:805px;top:36px;width:385px;height:130px;background:var(--green)">
    <svg style="position:absolute;inset:0;width:100%;height:100%" viewBox="0 0 385 130" preserveAspectRatio="none"><path d="M0 0H385V40Q192 140 0 40Z" fill="var(--ink)"/><path d="M0 40Q192 140 385 40V130H0Z" fill="var(--paper)"/></svg>
  </section>

  <!-- envelope back plain flap -->
  <section class="sheet envelope" style="left:805px;top:180px;width:385px;height:110px">
    <svg style="position:absolute;inset:0;width:100%;height:100%" viewBox="0 0 385 110" preserveAspectRatio="none"><path d="M0 0H385V30Q192 110 0 30Z" fill="#f4f4f4" stroke="#ddd"/></svg>
    <div class="brand-stack" style="position:absolute;left:0;width:100%;top:64px;font-size:8px"><span class="dot" style="width:7px;height:7px"></span>TMB</div>
  </section>

  <!-- envelope front -->
  <section class="sheet envelope" style="left:805px;top:305px;width:385px;height:112px">
    <div class="brand-stack" style="position:absolute;left:22px;top:12px;font-size:10px"><span class="dot" style="width:9px;height:9px"></span>TMB<span class="corp" style="font-size:4px;margin-top:1px">Corp</span></div>
    <div class="contact" style="left:16px;top:46px">2716 Bellhaven Lane<br>Simi Valley, CA 93063</div>
    <svg class="wave" style="bottom:0;height:34px" viewBox="0 0 385 34" preserveAspectRatio="none"><path d="M0 34V18Q200 30 385 4V34Z" fill="url(#gc)"/><path d="M0 14Q200 26 385 0" stroke="var(--ink)" stroke-width="2" fill="none"/></svg>
  </section>
  <p class="label" style="left:805px;top:424px;width:385px">Envelope Option 3</p>
</main>
</body>
</html>
```